Updated Business Card Re-design (Logo Provided)

I am needing to update our business cards for our practice, Bright Harbor Care. We are a personal injury and wellness practice. The final design should be elegant and classy, but a type of card people would want to keep. Any samples should only have Dr. Tarek Minouvel on the template.
Updates

Went on vacation/holiday

Need extra days to review

Target Market(s)

Personal Injury clients, wellness clients

Industry/Entity Type

Personal Injury, medical, wellness

Contact Information for Business Card

dr and practice name, offerings

Requirements
Must have
• Single sided, this will be printed on a transparent business card, no exceptions.

```html
<!DOCTYPE html>
<html lang="en">
<head>
<meta charset="utf-8">
<title>Bright Harbor Care – Business Card</title>
<link rel="stylesheet" href="https://fonts.googleapis.com/css2?family=Poppins:wght@300;400;600;700&display=swap">
<style>
  :root {
    --backdrop: #e7e3dd;
    --card-light-top: #f2f3f5;
    --card-light-bottom: #dcdee2;
    --blue-deep: #0b416f;
    --blue-mid: #15578f;
    --brand-blue: #1f5f95;
    --accent-orange: #dd6a1c;
    --ink-light: #ddd6c8;
    --ink-soft: #d2ccc0;
    --rule: #cfc8ba;
  }
  * { margin: 0; padding: 0; box-sizing: border-box; }
  html, body { width: 1200px; height: 867px; overflow: hidden; }
  body {
    background: var(--backdrop);
    font-family: "Poppins", sans-serif;
    position: relative;
  }
  .card {
    position: absolute;
    left: 120px; top: 193px;
    width: 962px; height: 535px;
    border-radius: 24px;
    overflow: hidden;
    background: linear-gradient(170deg, var(--card-light-top), var(--card-light-bottom));
    box-shadow: 0 6px 24px rgba(0,0,0,0.12);
  }
  .contact-panel {
    position: absolute;
    left: 470px; top: 0;
    width: 492px; height: 100%;
    background: linear-gradient(160deg, var(--blue-deep) 0%, var(--blue-mid) 100%);
  }
  .accent-tab {
    position: absolute;
    left: 447px; top: 142px;
    width: 52px; height: 255px;
    border-radius: 26px;
    background: var(--accent-orange);
    box-shadow: 0 0 0 10px var(--blue-deep);
    clip-path: inset(-12px -12px -12px -12px);
  }
  .brand {
    position: absolute;
    left: 0; top: 150px;
    width: 454px;
    text-align: center;
  }
  .brand-dot {
    display: block;
    width: 34px; height: 34px;
    margin: 0 auto 22px;
    border-radius: 50%;
    background: var(--accent-orange);
  }
  .brand-name {
    color: var(--brand-blue);
    font-weight: 700;
    font-size: 34px;
    line-height: 1.15;
    letter-spacing: -0.5px;
    text-transform: uppercase;
  }
  .person {
    position: absolute;
    left: 560px; top: 152px;
    width: 360px;
  }
  .person-name {
    color: var(--ink-light);
    font-weight: 700;
    font-size: 27px;
    letter-spacing: 0.3px;
    text-transform: uppercase;
    line-height: 1.2;
  }
  .person-role {
    margin-top: 8px;
    color: var(--ink-soft);
    font-size: 10px;
    font-weight: 400;
    text-transform: uppercase;
    letter-spacing: 0.2px;
  }
  .divider {
    position: absolute;
    left: 562px; top: 242px;
    width: 356px; height: 2px;
    background: var(--rule);
  }
  .details {
    position: absolute;
    left: 560px; top: 276px;
    color: var(--ink-light);
    font-weight: 300;
    font-size: 18.5px;
    line-height: 26px;
    list-style: none;
  }
  .address { margin-bottom: 6px; }
  .detail-line {
    display: flex;
    align-items: center;
    gap: 12px;
    height: 30px;
  }
  .detail-line svg { width: 14px; height: 14px; flex: none; fill: var(--accent-orange); }
</style>
</head>
<body>
  <div class="card">
    <div class="contact-panel"></div>
    <div class="accent-tab"></div>

    <div class="brand">
      <span class="brand-dot"></span>
      <div class="brand-name">Bright Harbor<br>Care</div>
    </div>

    <div class="person">
      <div class="person-name">Dr. Tarek Minouvel</div>
      <div class="person-role">Wellness Coach , Consultant &amp; Trainer</div>
    </div>
    <div class="divider"></div>

    <ul class="details">
      <li class="address">2418 Linden Quay Road<br>Port Averly, VA 23999</li>
      <li class="detail-line">
        <svg viewBox="0 0 16 16" aria-hidden="true"><path d="M1 6c0-2 3-4 7-4s7 2 7 4v1h-4V5.5H5V7H1z M3 8h10l1 6H2z"/></svg>
        <span>555-014-2267</span>
      </li>
      <li class="detail-line">
        <svg viewBox="0 0 16 16" aria-hidden="true"><path d="M8 1a7 7 0 1 0 0 14A7 7 0 0 0 8 1zm0 1.5c.8 0 1.8 1.7 2 4.5H6c.2-2.8 1.2-4.5 2-4.5zM2.6 7h2C4.7 5 5 3.7 5.6 3 4 3.8 2.9 5.2 2.6 7zm8.8 0h2c-.3-1.8-1.4-3.2-3-4 .6.7 1 2 1 4zM2.6 9c.3 1.8 1.4 3.2 3 4-.6-.7-.9-2-1-4zm3.4 0c.2 2.8 1.2 4.5 2 4.5s1.8-1.7 2-4.5zm5.4 0c-.1 2-.4 3.3-1 4 1.6-.8 2.7-2.2 3-4z"/></svg>
        <span>brightharborcare.example</span>
      </li>
      <li class="detail-line">
        <svg viewBox="0 0 16 16" aria-hidden="true"><path d="M1 3h14v10H1z M2.5 4.5 8 9l5.5-4.5v-.3H2.5z" fill-rule="evenodd"/></svg>
        <span>hello@brightharborcare.example</span>
      </li>
    </ul>
  </div>
</body>
</html>
```